Online Advice via Video Site requires Cutting Edge Homepage

We need a creative new and exciting webdesign for our tutoring via video-chat website.

We have prepared a "demo" homepage for you to see various promotional material that we think would be suitable for the homepage. http://www.quizlanterna.com/demo

The actual site is undergoing some final tinkering but can be accessed and used at http://www.quizlanterna.com

There is NO NEED to take any colours or design structure from this.

We expect the logo to be changed to match the new site. The new logo should match the site's function.

I have included some other projects that we like the look of:
http://www.artflockly.com.au/design/143762
http://www.artflockly.com.au/design/561630
http://www.artflockly.com.au/design/247199
http://www.artflockly.com.au/design/255195
http://www.bravolumo.tv/

Target Market(s)

People that will work as tutors/advisers or be student/clients

Industry/Entity Type

Tutoring

Requirements
Must have
• The search is the main feature of the homepage

After the search the next goal of the page is to get people to sign up to the site

Login, (optional inclusion of the chatterbox login - if you don't include it then you need only have a "login" button... no username or password input fields)

Footer
Nice to have
• The promotional material for the site, the colours on the Slidora file CAN BE changed to suit the new design you propose.

```html
<!DOCTYPE html>
<html lang="en">
<head>
<meta charset="utf-8">
<title>Quiz Lanterna – Home</title>
<link href="https://fonts.googleapis.com/css2?family=Arimo:wght@400;700&display=swap" rel="stylesheet">
<style>
:root{
  --page:#ffffff;
  --teal:#2b8fa6;
  --teal-light:#6cc3d3;
  --teal-dark:#0f5668;
  --panel:#1d6f87;
  --grey:#e6e8ea;
  --grey-mid:#c9cdd1;
  --ink:#2b2b2b;
  --footer:#0b0b0b;
  --footer-text:#e8e8e8;
}
*{box-sizing:border-box;margin:0;padding:0}
html,body{width:900px;height:1200px;overflow:hidden}
body{background:var(--page);font-family:"Arimo",Arial,sans-serif;color:var(--ink);position:relative}
.abs{position:absolute}
.brand{left:180px;top:18px;display:flex;align-items:center;gap:12px}
.brand-mark{width:60px;height:60px;border-radius:50%;background:var(--teal)}
.brand-name{font-size:30px;color:var(--ink)}
.share{left:594px;top:14px;width:150px;height:120px;background:var(--grey);border:1px solid var(--grey-mid);padding:8px;font-size:10px}
.share .icons{display:flex;gap:4px;margin:8px 0}
.share .icons span{width:14px;height:14px;background:var(--teal)}
.share .btn{display:inline-block;margin-top:6px;background:var(--teal-dark);color:#fff;padding:3px 6px;font-size:10px;font-weight:700}
.nav{left:171px;top:138px;width:573px;height:26px;background:linear-gradient(#f2f3f4,#d2d6d9);border-radius:4px;text-align:center;font-size:15px;font-weight:700;line-height:26px}
.nav a{color:var(--ink);text-decoration:none}
.nav a.current{color:var(--teal)}
.banner{left:171px;top:171px;width:573px;height:279px;background:linear-gradient(120deg,#0e0e0e,#3a3a3a 60%,#1b1b1b)}
.quote{left:440px;top:200px;width:290px;color:#fff;font-size:23px;font-weight:700;font-style:italic;text-align:center;line-height:1.25}
.search{left:171px;width:573px;height:30px;background:var(--grey);border-radius:15px;display:flex;align-items:center;padding:0 10px;gap:10px}
.search .label{color:var(--teal);font-weight:700;font-size:14px;margin-left:150px}
.search .field{flex:1;height:18px;background:#fff;border:1px solid var(--grey-mid)}
.search .go{background:var(--teal);color:#fff;font-size:11px;padding:5px 14px;border-radius:12px}
.feature{left:171px;top:492px;width:240px;height:345px;background:var(--panel);border-radius:6px;color:#fff;padding:10px;font-size:10px;overflow:hidden}
.feature .photo{height:78px;background:linear-gradient(#e9eef0,#b9c7cc);margin-bottom:9px}
.feature p{margin-bottom:6px;line-height:1.3}
.feature h3{font-size:11px;margin:9px 0 7px;text-align:center}
.feature ul{margin:0}
.feature li{list-style:none;font-weight:700;color:var(--teal-light);font-size:11px;line-height:14px;margin:0 0 4px 30px}
.col{width:165px;border-radius:6px;padding:10px;font-size:9px;line-height:1.35}
.col h4{font-size:10px;margin-bottom:8px}
.col .more{margin-top:8px;font-weight:700}
.dark{background:var(--teal-dark);color:#fff}
.light{background:var(--grey);color:var(--ink)}
.footer{left:0;top:885px;width:900px;height:315px;background:var(--footer);color:var(--footer-text)}
.footer h5{font-size:15px;position:absolute;top:10px}
.enquiry{left:150px}
.form-row{position:absolute;left:160px;font-size:14px}
.input{position:absolute;left:240px;width:160px;height:22px;background:#fff}
.submit{left:352px;top:223px;background:var(--teal);color:#fff;font-size:11px;padding:4px 10px}
.links{position:absolute;left:425px;top:48px;font-size:11px;line-height:22px}
.social{position:absolute;left:530px;top:40px;font-size:11px}
.social div{display:flex;align-items:center;gap:10px;height:41px}
.social span{width:20px;height:20px;background:var(--teal)}
.rule{position:absolute;top:0;width:1px;height:270px;background:#444}
.bottom{position:absolute;left:0;top:272px;width:900px;height:43px;background:#1a1a1a;font-size:9px;text-align:right;padding:15px 130px}
</style>
</head>
<body>
<div class="abs brand"><span class="brand-mark"></span><span class="brand-name">Quiz Lanterna</span></div>

<div class="abs share">
  <strong>Share This</strong>
  <div class="icons"><span></span><span></span><span></span><span></span><span></span></div>
  <div>Sign In With Chatterbox</div>
  <span class="btn">Chatterbox</span>
</div>

<nav class="abs nav"><a class="current" href="#">Home</a> | <a href="#">Student</a> | <a href="#">Advisors</a> | <a href="#">Topics</a> | <a href="#">Blog</a></nav>

<div class="abs banner" role="img" aria-label="Photo of a chalkboard covered in maths equations with a hand writing"></div>
<p class="abs quote">"Imagine if, whenever you had a problem you could instantly access the world's experts to solve it. Now you can!</p>

<div class="abs search" style="top:454px"><span class="label">SEARCH</span><span class="field"></span><span class="go">Search Topics and Advisors</span></div>

<section class="abs feature">
  <div class="photo" role="img" aria-label="Photo of a group of smiling students"></div>
  <p>Quiz Lanterna is the place for e-learning, mentoring &amp; professional advice.</p>
  <p>• Instantly connect people with knowledge and those who need it.</p>
  <p>• Connect people for ongoing advice or one-off sessions.</p>
  <p>• Ask questions and get answers when it suits you.</p>
  <h3>SEARCH ADVISORS BY TOPIC</h3>
  <ul><li>Mathematics</li><li>English</li><li>Languages</li><li>Technology</li></ul>
</section>

<section class="abs col dark" style="left:420px;top:492px;height:165px">
  <h4>ADVISORS</h4>
  <p>Earn an income sharing what you know. Set your own hours and rates, build a profile and connect with students across the globe from home.</p>
  <p class="more">Read More</p>
</section>
<section class="abs col dark" style="left:420px;top:665px;height:172px">
  <h4>CLIENTS</h4>
  <p>Find the right expert in minutes. Browse by topic, compare reviews and start a live video session whenever you need help the most.</p>
  <p class="more">Read More</p>
</section>
<section class="abs col light" style="left:591px;top:492px;width:153px;height:180px">
  <h4>STUDENTS</h4>
  <p>• Get help with homework fast<br>• Book tutors in any subject<br>• Learn at your own pace<br>• Review recorded lessons<br>• Pay only for the time used</p>
  <p class="more">Read More</p>
</section>
<section class="abs col light" style="left:591px;top:680px;width:153px;height:157px">
  <h4>ADVISORS</h4>
  <p>• Share your knowledge<br>• Set your schedule<br>• Choose your own rates<br>• Grow a loyal client base</p>
  <p class="more">Read More</p>
</section>

<div class="abs search" style="top:842px"><span class="label">SEARCH</span><span class="field"></span><span class="go">Search Topics and Advisors</span></div>

<footer class="abs footer">
  <h5 class="enquiry">QUICK ENQUIRY</h5>
  <span class="form-row" style="top:64px">Name:</span><span class="input" style="top:62px"></span>
  <span class="form-row" style="top:89px">E-mail:</span><span class="input" style="top:87px"></span>
  <span class="form-row" style="top:114px">Comments:</span><span class="input" style="top:114px;height:100px"></span>
  <span class="abs submit">Submit</span>
  <span class="rule" style="left:412px"></span>
  <h5 style="left:420px">QUICK LINKS</h5>
  <div class="links">HOME<br>STUDENT<br>ADVISORS<br>TOPICS<br>BLOG</div>
  <span class="rule" style="left:525px"></span>
  <h5 style="left:532px">SOCIALISE</h5>
  <div class="social">
    <div><span></span>LINKLY</div>
    <div><span></span>CHATTERBOX</div>
    <div><span></span>SNAPFLOW</div>
    <div><span></span>TAGSTASH</div>
    <div><span></span>POSTPAD</div>
  </div>
  <div class="bottom">Quiz Lanterna © 2012 | Terms | Sitemap | About us | Our Technology | Contact</div>
</footer>
</body>
</html>
```